Lumentide

We have already had a logo designed. Attached is the logo.
We are now wanting to design a label that will wrap around a plastic bottle which contains 1 litre of fluid. The size of the label is 15cm high by 28 cm wide.
The bottle for which the label will be used is a natural wellbeing supplement in a class of its own. It is a liquid tonic/complementary medicine - not a drink you guzzle down like zestorade.
The label needs to look natural and healthy and include the logo attached.
This is a premium bottle which will cost more than $50 AUD per bottle. The label needs to be classy as you would expect to find on an expensive bottle of wine.
The label needs to be able to sell the bottle and it needs to convince that what is inside the bottle is worth what it will cost.
The product does not have fruit in it and is not a water drink. One of the ingredients is an extract from the French Maritime Pine Bark.
We do not want the label to be to busy.
The product is to market in China, United States and Australia.
We will have to typeset certain wording onto the label - Ingredients, company details, bottle code etc which will be on the back of the bottle.
Updates

We have uploaded a picture of the plastic bottle that the label will be used on. The dimensions of the label have been included in the project brief.

Regards

Reason: We realise that the time period allowed to create a label may have been to short for some designers. Thanks

Reason: Just waiting on final designs to be submitted. This will be the last extension. Regards

Target Market(s)

Generally adults aged 35 to 65.

Industry/Entity Type

Plastic

Requirements
Must have
• Most of this information has been outlined above.

```html
<!DOCTYPE html>
<html lang="en">
<head>
<meta charset="utf-8">
<title>Lumentide – Bottle Label</title>
<link rel="stylesheet" href="https://fonts.googleapis.com/css2?family=Open+Sans:wght@700&family=Crimson+Text:ital,wght@1,700&display=swap">
<style>
  :root {
    --page-bg: #f4f4f2;
    --label-white: #fbfbf8;
    --plum-deep: #7e1150;
    --plum-light: #c58aa9;
    --leaf-green: #7ab648;
    --leaf-light: #a3cf63;
    --forest-green: #1e6b3a;
    --foliage-dark: #3f8a2a;
    --bullet-plum: #7a1448;
  }
  * { margin: 0; padding: 0; box-sizing: border-box; }
  html, body {
    width: 1200px;
    height: 900px;
    overflow: hidden;
    background: var(--page-bg);
  }
  .canvas {
    position: relative;
    width: 1200px;
    height: 900px;
  }
  .label {
    position: absolute;
    left: 370px;
    top: 20px;
    width: 460px;
    height: 860px;
    background: var(--label-white);
    overflow: hidden;
    box-shadow: 0 2px 14px rgba(0,0,0,0.08);
  }
  .label-art {
    position: absolute;
    inset: 0;
  }
  .brand {
    position: absolute;
    top: 248px;
    left: 0;
    width: 100%;
    text-align: center;
  }
  .brand-dot {
    display: block;
    width: 30px;
    height: 30px;
    margin: 0 auto 12px;
    border-radius: 50%;
    background: var(--leaf-green);
  }
  .brand-name {
    font-family: "Open Sans", sans-serif;
    font-weight: 700;
    font-size: 54px;
    letter-spacing: 0.5px;
    color: var(--forest-green);
    line-height: 1;
  }
  .benefits {
    position: absolute;
    top: 420px;
    left: 64px;
    list-style: none;
    font-family: "Crimson Text", serif;
    font-style: italic;
    font-weight: 700;
    font-size: 18px;
    line-height: 29px;
    color: var(--bullet-plum);
  }
  .benefits li {
    position: relative;
    padding-left: 18px;
  }
  .benefits li::before {
    content: "";
    position: absolute;
    left: 0;
    top: 11px;
    width: 8px;
    height: 8px;
    border-radius: 50%;
    background: var(--leaf-green);
  }
  .volume {
    position: absolute;
    right: 46px;
    bottom: 26px;
    font-family: "Open Sans", sans-serif;
    font-weight: 700;
    font-size: 28px;
    color: var(--bullet-plum);
  }
</style>
</head>
<body>
<main class="canvas">
  <section class="label">
    <svg class="label-art" width="460" height="860" viewBox="0 0 460 860">
      <defs>
        <linearGradient id="plum-band" x1="0" y1="0" x2="1" y2="0">
          <stop offset="0" stop-color="var(--plum-deep)"/>
          <stop offset="1" stop-color="var(--plum-light)"/>
        </linearGradient>
        <linearGradient id="green-wave" x1="0" y1="1" x2="1" y2="0">
          <stop offset="0" stop-color="var(--leaf-green)"/>
          <stop offset="1" stop-color="var(--leaf-light)"/>
        </linearGradient>
        <linearGradient id="foliage" x1="0" y1="0" x2="0" y2="1">
          <stop offset="0" stop-color="var(--foliage-dark)"/>
          <stop offset="0.45" stop-color="var(--leaf-green)"/>
          <stop offset="0.8" stop-color="#dcebcf"/>
          <stop offset="1" stop-color="var(--label-white)"/>
        </linearGradient>
      </defs>
      <path class="plum-band" d="M0 0 H460 V30 C300 50 130 140 0 268 Z" fill="url(#plum-band)"/>
      <path class="green-swoosh" d="M70 216 C92 146 160 100 236 88 C310 76 390 52 460 36 V46 C392 64 318 90 256 104 C186 122 120 164 70 216 Z" fill="var(--leaf-green)"/>
      <path class="green-wave" d="M0 640 C160 600 350 500 460 350 V720 H0 Z" fill="url(#green-wave)"/>
      <path class="foliage-row" d="M0 660 C40 640 70 610 110 600 C150 610 170 580 210 560 C250 575 280 545 320 530 C360 545 400 520 460 520 V820 H0 Z" fill="url(#foliage)" role="img" aria-label="Row of stylised green leaves rising along the base of the label"/>
    </svg>

    <div class="brand">
      <span class="brand-dot"></span>
      <h1 class="brand-name">Lumentide</h1>
    </div>

    <ul class="benefits">
      <li>Busa voluptat facerum</li>
      <li>Quatur erit fugiati</li>
      <li>Andipsam fugit pellandipit</li>
      <li>Labor aut ratus eatem</li>
    </ul>

    <p class="volume">1l</p>
  </section>
</main>
</body>
</html>
```